Coral Tidewave Stationary

Recently established Aquatics Club, with competitive swimming being a principal activity needs stationary, including business cards, letterhead and envelopes, application forms.
The designs shold incorporate the Club's logo. ( The colours are aqua and teal)
The statonary should be fun yet project a corporate image sufficient to attract potential sponsors.

Target Market(s)

Club members, sponsors, professional organisations.

Industry/Entity Type

Business

Requirements
Must have
• Club Logo
Address & Telephone number

The letterhead must contain the Club's Mission Statement.
It can be incorporated in the "footer" on the page.

To provide aquatics programmes, for persons of all ages, that encourage physical fitness and wellness, build character and self-discipline, inspire camaraderie and promote civic mindedness and excellence.

```html
<!DOCTYPE html>
<html lang="en">
<head>
<meta charset="utf-8">
<title>Coral Tidewave Letterhead</title>
<link href="https://fonts.googleapis.com/css2?family=Arimo:wght@400;700&display=swap" rel="stylesheet">
<style>
  :root {
    --page-peach: #fde6d2;
    --sheet-cream: #fdf3ea;
    --ring-tint: #f9d8bd;
    --brand-orange: #ef7f22;
    --wedge-orange: #f7902e;
    --teal-deep: #0f8a84;
    --teal-light: #35b3aa;
  }
  html, body {
    margin: 0;
    padding: 0;
    overflow: hidden;
    background: var(--page-peach);
  }
  .letterhead {
    position: relative;
    width: 927px;
    height: 1200px;
    overflow: hidden;
    background: var(--page-peach);
    font-family: "Arimo", Arial, sans-serif;
  }
  .letterhead__frame {
    position: absolute;
    inset: 0;
    width: 927px;
    height: 1200px;
  }
  .brand-name {
    position: absolute;
    left: 62px;
    top: 92px;
    margin: 0;
    font-weight: 700;
    font-size: 38px;
    line-height: 1.05;
    color: var(--brand-orange);
  }
  .header-note {
    position: absolute;
    right: 44px;
    top: 88px;
    width: 600px;
    margin: 0;
    text-align: right;
    font-size: 10px;
    line-height: 1.45;
    color: var(--brand-orange);
  }
  .art-area {
    position: absolute;
  }
  .art-area--swoosh {
    left: 0;
    top: 500px;
    width: 171px;
    height: 100px;
    border-radius: 0 50px 50px 0;
    background: linear-gradient(90deg, var(--brand-orange), var(--wedge-orange));
  }
  .art-area--splash {
    left: 160px;
    top: 800px;
    width: 200px;
    height: 90px;
    border-radius: 45px;
    background: linear-gradient(135deg, var(--teal-deep), var(--teal-light));
    opacity: 0.85;
  }
  .art-area--waves {
    left: 0;
    top: 970px;
    width: 927px;
    height: 230px;
    border-radius: 60% 40% 0 0 / 60px 60px 0 0;
    background: linear-gradient(135deg, var(--teal-deep), var(--teal-light));
  }
  .letter-footer {
    position: absolute;
    left: 380px;
    top: 806px;
    width: 480px;
    margin: 0;
    font-size: 10px;
    line-height: 1.5;
    color: var(--teal-deep);
    text-align: right;
  }
  .letter-footer__mission {
    margin: 0 0 8px;
    font-style: normal;
  }
  .letter-footer__contact {
    margin: 0;
    font-weight: 700;
    color: var(--brand-orange);
    font-style: normal;
  }
</style>
</head>
<body>
<main class="letterhead">
  <svg class="letterhead__frame" viewBox="0 0 927 1200" xmlns="http://www.w3.org/2000/svg" aria-hidden="true">
    <circle class="ring ring--small" cx="538" cy="131" r="130" fill="none" stroke="var(--ring-tint)" stroke-width="50" opacity="0.8"/>
    <circle class="ring ring--large" cx="835" cy="5" r="175" fill="none" stroke="var(--ring-tint)" stroke-width="45" opacity="0.8"/>
    <polygon class="sheet" points="26,145 806,76 894,1200 124,1200" fill="var(--sheet-cream)" opacity="0.9"/>
  </svg>

  <div class="art-area art-area--swoosh" role="img" aria-label="Orange swoosh decoration at the left edge"></div>
  <div class="art-area art-area--splash" role="img" aria-label="Teal water droplet decoration"></div>
  <div class="art-area art-area--waves" role="img" aria-label="Teal wave decoration along the foot of the page"></div>

  <h1 class="brand-name">Coral<br>Tidewave</h1>

  <p class="header-note">Lorem ipsum dolor sit amet, consectetur adipiscing elit. Aenean pellentesque ligula sed risus pharetra ac porta neque aliquam.<br>Cras ornare felis id libero hendrerit fringi</p>

  <footer class="letter-footer">
    <p class="letter-footer__mission">To provide aquatics programmes, for persons of all ages, that encourage physical fitness and wellness, build character and self-discipline, inspire camaraderie and promote civic mindedness and excellence.</p>
    <address class="letter-footer__contact">14 Harbour Lane, Bayside &nbsp;|&nbsp; Tel: 555 0142 678</address>
  </footer>
</main>
</body>
</html>
```